Business Card for Amber Finch Advisors

Business card design for Amber Finch Advisors, a new consulting and financial advisory firm. I would like the designs to integrate the logo attached (at least on 1 side).

Target Market(s)

individual and institutional clients

Contact Information for Business Card

Daniel R. Hollis, CFA
Managing Director
amberfinchadvisors.comp
hollis@amberfinchadvisors.example
(555) 217-4630

```html
<!DOCTYPE html>
<html lang="en">
<head>
<meta charset="utf-8">
<title>Amber Finch Advisors — Business Card</title>
<link rel="stylesheet" href="https://fonts.googleapis.com/css2?family=Arimo:wght@400;700&display=swap">
<style>
  :root {
    --backdrop: #8a8a8a;
    --card-dark: #1c1c1c;
    --card-dark-edge: #262626;
    --card-light: #ffffff;
    --amber: #e8781e;
    --ink: #111111;
    --paper-text: #ffffff;
  }
  * { box-sizing: border-box; margin: 0; padding: 0; }
  html, body {
    width: 1200px; height: 997px; overflow: hidden;
    background: var(--backdrop);
    font-family: "Arimo", Arial, sans-serif;
  }
  .canvas { position: relative; width: 1200px; height: 997px; }
  .card {
    position: absolute; width: 548px; height: 328px;
    border-radius: 20px; overflow: hidden;
    background: radial-gradient(ellipse at 50% 40%, var(--card-dark-edge), var(--card-dark));
  }
  .card--front { left: 335px; top: 84px; }
  .card--back { left: 336px; top: 478px; }
  .front-shapes { position: absolute; inset: 0; }
  .holder { position: absolute; left: 21px; top: 36px; }
  .holder__name { color: var(--amber); font-weight: 700; font-size: 17px; }
  .holder__title { color: var(--paper-text); font-size: 14px; margin-top: 5px; }
  .firm-name {
    color: var(--amber); font-weight: 400; white-space: nowrap; letter-spacing: 0.5px;
  }
  .card--front .firm-name {
    position: absolute; right: 31px; top: 130px; font-size: 24px;
  }
  .contact { position: absolute; right: 31px; font-size: 12px; font-weight: 700; color: var(--ink);
    display: flex; align-items: center; gap: 17px; }
  .contact--phone { top: 244px; }
  .contact--email { top: 279px; }
  .contact__icon {
    width: 21px; height: 21px; border-radius: 4px; background: var(--ink);
    display: flex; align-items: center; justify-content: center;
  }
  .card--back .firm-name {
    position: absolute; left: 0; right: 0; top: 146px; text-align: center; font-size: 34px;
  }
</style>
</head>
<body>
<main class="canvas">
  <section class="card card--front" aria-label="Card front">
    <svg class="front-shapes" width="548" height="328" viewBox="0 0 548 328">
      <path d="M360 0 L548 0 L548 328 L0 328 L0 298 C110 150 250 40 360 0 Z" fill="var(--card-light)"/>
      <path d="M495 16 C300 30 110 130 0 244 L0 290 C100 160 280 40 495 16 Z" fill="var(--amber)"/>
    </svg>
    <div class="holder">
      <p class="holder__name">Daniel R. Hollis, CFA</p>
      <p class="holder__title">Managing Director</p>
    </div>
    <p class="firm-name">Amber Finch Advisors</p>
    <p class="contact contact--phone">(555) 217-4630
      <span class="contact__icon">
        <svg width="13" height="13" viewBox="0 0 24 24"><path fill="#fff" d="M6.6 10.8a15 15 0 0 0 6.6 6.6l2.2-2.2c.3-.3.7-.4 1-.2 1.1.4 2.3.6 3.6.6.6 0 1 .4 1 1V20c0 .6-.4 1-1 1A17 17 0 0 1 3 4c0-.6.4-1 1-1h3.5c.6 0 1 .4 1 1 0 1.3.2 2.5.6 3.6.1.3 0 .7-.2 1z"/></svg>
      </span>
    </p>
    <p class="contact contact--email">hollis@amberfinchadvisors.example
      <span class="contact__icon">
        <svg width="13" height="13" viewBox="0 0 24 24"><rect x="2" y="5" width="20" height="14" rx="2" fill="#fff"/><path d="M2 6l10 7 10-7" stroke="#111" stroke-width="2" fill="none"/></svg>
      </span>
    </p>
  </section>

  <section class="card card--back" aria-label="Card back">
    <p class="firm-name">Amber Finch Advisors</p>
  </section>
</main>
</body>
</html>
```